New flavour! New packaging for Velocity Energy Drink!

We need a new packaging designed to show off our new grape flavored energy drink! It will require box design with matching sachets!

Established in 2018 we are a fully Australian owned and operated business that started out with 2 gamers that got sick and tired of sugary energy drinks OR expensive powder from the USA.

We are an energy drink in the esports and gaming space. Our new product is an energy drink in powder in boxes of 30 sachets (please see attached for product example)

Please see example 1 and 2 for our competitors product. We would ideally like to go a bit more minimalist than them but still have a great color pop on black backing.

Target Market(s)

Gamer's and esports athletes between the ages or 18-30

Font styles to use
Sans Serif
Other font styles liked:
• Helvetica

Colors
886aae
ffffff

Requirements
Must have
• Black base/background.
• Vibrant purple N in the Velocity Logo.
• Same or slightly different shades of purple for some text and highlights.
• Black, white and some shades of a vibrant purple (for the grape flavor)
• ingredients list (may need to be reformatted to suit)
• Please see attached for legislative requirements on the box and sachets.
Nice to have
• minimalist design but enough to be eye catching and somewhat playful
• Twitter: @VLCT_FUEL
• Instagram: @VLCT_FUEL
• Facebook: @VLCTFUEL
Should not have
• OTHER COLORS.
• Overly complex designs.

```html
<!DOCTYPE html>
<html lang="en">
<head>
<meta charset="utf-8">
<title>Velocity Energy Drink – Grape Packaging</title>
<link href="https://fonts.googleapis.com/css2?family=Montserrat:wght@300;400;600;700;800&family=Quicksand:wght@400;500;600&display=swap" rel="stylesheet">
<style>
  :root {
    --bg: #d6d6d6;
    --black: #050505;
    --purple: #886aae;
    --purple-deep: #6f54a0;
    --lavender: #dccbf7;
    --white: #ffffff;
    --muted: #cfcfcf;
  }
  * { box-sizing: border-box; margin: 0; padding: 0; }
  html, body { width: 1200px; height: 900px; overflow: hidden; background: var(--bg); }
  .canvas { position: relative; width: 1200px; height: 900px; background: var(--bg); font-family: "Montserrat", sans-serif; color: var(--white); }

  .panel { position: absolute; top: 40px; height: 570px; background: var(--black); overflow: hidden; }
  .spine-left { left: 160px; width: 90px; }
  .front { left: 270px; width: 320px; }
  .back { left: 610px; width: 330px; }
  .spine-right { left: 960px; width: 80px; }

  /* wordmark */
  .wordmark { display: flex; align-items: center; gap: 8px; font-family: "Montserrat", sans-serif; font-weight: 800; color: var(--white); letter-spacing: 1px; line-height: 1; }
  .wordmark .mark { width: 0.7em; height: 0.7em; background: var(--purple); flex: none; }

  .spine-left .wordmark { position: absolute; left: 50%; top: 58%; font-size: 34px; transform: translate(-50%, -50%) rotate(-90deg); white-space: nowrap; }

  /* front */
  .front .corner { position: absolute; inset: 0; }
  .front .headline { position: absolute; left: 118px; top: 58px; height: 240px; writing-mode: vertical-rl; transform: rotate(180deg); display: flex; gap: 2px; }
  .headline .title { font-weight: 700; font-size: 38px; letter-spacing: 3px; color: var(--lavender); line-height: 1; }
  .headline .flavour { font-weight: 700; font-size: 20px; letter-spacing: 2px; color: var(--lavender); line-height: 1.05; }
  .headline .extras { font-weight: 700; font-size: 18px; letter-spacing: 2px; color: var(--white); line-height: 1.05; }
  .front .block { position: absolute; left: 110px; top: 320px; width: 110px; height: 110px; background: var(--purple); }
  .tagline { font-weight: 300; color: var(--lavender); line-height: 1.05; }
  .tagline b { font-weight: 400; }
  .front .tagline { position: absolute; right: 24px; top: 452px; font-size: 25px; }
  .front .net { position: absolute; left: 134px; top: 520px; font-size: 15px; font-weight: 400; letter-spacing: 0.5px; }

  /* back */
  .back { padding: 26px 22px 0 22px; font-family: "Quicksand", sans-serif; }
  .back .wordmark { font-size: 34px; justify-content: center; margin-bottom: 20px; }
  .panel-heading { font-size: 9px; text-transform: uppercase; letter-spacing: 0.3px; }
  .nutrition { width: 100%; border-collapse: collapse; font-size: 7.5px; text-transform: uppercase; }
  .nutrition td, .nutrition th { padding: 1px 2px; font-weight: 500; text-align: left; border-bottom: 1px solid var(--lavender); vertical-align: bottom; }
  .nutrition td.num, .nutrition th.num { text-align: center; width: 62px; }
  .nutrition th { font-weight: 500; font-size: 7px; line-height: 1.1; }
  .nutrition .indent { padding-left: 18px; text-transform: none; }
  .nutrition .plain { text-transform: none; }
  .nutrition .section td { border-bottom: 2px solid var(--lavender); padding-top: 6px; }
  .nutrition .rule-top td { border-top: 2px solid var(--lavender); }
  .label-block { margin-top: 7px; font-size: 7.6px; line-height: 1.2; }
  .label-block .tag { display: inline-block; background: var(--lavender); color: var(--black); font-size: 7.5px; font-weight: 600; text-transform: uppercase; padding: 0 3px; margin-bottom: 1px; }
  .label-block p { padding-left: 8px; }
  .importer { margin-top: 22px; font-family: "Montserrat", sans-serif; font-size: 7.5px; line-height: 1.3; color: var(--muted); padding-left: 8px; }
  .importer .origin { margin-top: 6px; }

  /* right spine */
  .socials { position: absolute; left: 50%; bottom: 60px; transform: translateX(-50%); display: flex; gap: 8px; }
  .social { display: flex; flex-direction: column; align-items: center; gap: 6px; }
  .social .icon { width: 14px; height: 14px; background: var(--purple); }
  .social .handle { writing-mode: vertical-rl; font-size: 8px; color: var(--white); letter-spacing: 0.3px; }

  /* sachet */
  .sachet { position: absolute; left: 210px; top: 672px; width: 780px; height: 118px; }
  .sachet svg { position: absolute; inset: 0; }
  .sachet .wordmark { position: absolute; left: 330px; top: 40px; font-size: 38px; }
  .sachet .tagline { position: absolute; right: 56px; top: 32px; font-size: 24px; }
</style>
</head>
<body>
<div class="canvas">

  <section class="panel spine-left" aria-label="Box side panel">
    <div class="wordmark"><span class="mark"></span>VELOCITY</div>
  </section>

  <section class="panel front" aria-label="Box front panel">
    <svg class="corner" viewBox="0 0 320 570" preserveAspectRatio="none" aria-hidden="true">
      <polygon points="35,0 190,0 80,152" fill="var(--purple)"/>
      <polygon points="35,0 80,0 80,152" fill="var(--purple-deep)"/>
    </svg>
    <div class="headline">
      <span class="title">ENERGY DRINK</span>
      <span class="flavour">GRAPE FLAVOUR</span>
      <span class="extras">WITH GINSENG CAFFEINE</span>
    </div>
    <div class="block"></div>
    <p class="tagline">for <b>GAMERS</b><br>by <b>GAMERS</b></p>
    <p class="net">150g / 5gx30 serves</p>
  </section>

  <section class="panel back" aria-label="Box back panel">
    <div class="wordmark"><span class="mark"></span>VELOCITY</div>
    <p class="panel-heading">Nutrition information</p>
    <table class="nutrition">
      <tr><td colspan="3">Servings per package:</td></tr>
      <tr class="rule-top"><td>Serving size</td><td colspan="2" class="plain" style="text-align:center">5g powder &amp; 500 ml water</td></tr>
      <tr><th></th><th class="num">Av quantity per serving (400ml)</th><th class="num">Av quantity per 100 ml</th></tr>
      <tr><td>Energy</td><td class="num">5kJ</td><td class="num">1kJ</td></tr>
      <tr><td>Protein</td><td class="num">0.0g</td><td class="num">0.0g</td></tr>
      <tr><td>Fat total</td><td class="num">0.0g</td><td class="num">0.0g</td></tr>
      <tr><td class="indent">Saturated fat</td><td class="num">0.0g</td><td class="num">0.0g</td></tr>
      <tr><td>Carbohydrate</td><td class="num">0.3g</td><td class="num">0.1g</td></tr>
      <tr><td class="indent">Sugars</td><td class="num">0.0g</td><td class="num">0.0g</td></tr>
      <tr><td>Sodium</td><td class="num">250mg</td><td class="num">62mg</td></tr>
      <tr class="section"><td colspan="3">Composition information</td></tr>
      <tr><td class="plain">Caffeine</td><td class="num">100mg</td><td class="num">25mg</td></tr>
      <tr><td class="plain">Thiamin (B1)</td><td class="num">10mg</td><td class="num">2.5mg</td></tr>
      <tr><td class="plain">Riboflavin (B2)</td><td class="num">5 mg</td><td class="num">1.2 mg</td></tr>
      <tr><td class="plain">Niacin (B3)</td><td class="num">20 mg</td><td class="num">5 mg</td></tr>
      <tr><td class="plain">B6 (Pyridoxine)</td><td class="num">5 mg</td><td class="num">1.2 mg</td></tr>
      <tr><td class="plain">Taurine</td><td class="num">500 mg</td><td class="num">125 mg</td></tr>
      <tr><td class="plain">Inositol</td><td class="num">50 mg</td><td class="num">12.5 mg</td></tr>
    </table>

    <div class="label-block">
      <span class="tag">Ingredient listing:</span>
      <p>Acidity regulator (citric acid, sodium citrate), mineral salt (sodium bicarbonate), taurine, natural orange juice powder (8.5%) (maltodextrin, sugar, orange juice concentrate), caffeine (2.8%), inositol, vitamins (B3, B1, B6, B2), ginseng extract (0.5%), sweetener (steviol glycoside), mineral salt (magnesium stearate).</p>
    </div>
    <div class="label-block">
      <span class="tag">Storage statement:</span>
      <p>Store in a cool dry place, away from sunlight below 25°C. Keep away from children.</p>
    </div>
    <div class="label-block">
      <span class="tag">Directions for use:</span>
      <p>Place one tablet in 400 ml water, stir until dissolved, and consume immediately.</p>
    </div>
    <div class="label-block">
      <span class="tag">Usage:</span>
      <p>Maximum of two SACHET per day</p>
    </div>
    <div class="importer">
      <p>Imported By:<br>Arcade Fuel Co Pty Ltd<br>27 Harbour Row<br>Docklands VIC 3008<br>Australia<br>www.velocityfuel.example</p>
      <p class="origin">Made in China</p>
    </div>
  </section>

  <section class="panel spine-right" aria-label="Box side panel with social handles">
    <div class="socials">
      <div class="social"><span class="icon"></span><span class="handle">@VLCTFUEL</span></div>
      <div class="social"><span class="icon"></span><span class="handle">@VLCT_FUEL</span></div>
      <div class="social"><span class="icon"></span><span class="handle">@VLCT_FUEL</span></div>
    </div>
  </section>

  <section class="sachet" aria-label="Single sachet">
    <svg viewBox="0 0 780 118" aria-hidden="true">
      <polygon fill="var(--black)" points="30,4 750,4 756,10 750,16 756,22 750,28 756,34 750,40 756,46 750,52 756,58 750,64 756,70 750,76 756,82 750,88 756,94 750,100 756,106 750,114 30,114"/>
      <polygon fill="var(--purple)" points="30,4 250,4 170,114 30,114 24,106 30,100 24,94 30,88 24,82 30,76 24,70 30,64 24,58 30,52 24,46 30,40 24,34 30,28 24,22 30,16 24,10"/>
      <rect x="30" y="4" width="22" height="110" fill="var(--purple-deep)"/>
      <rect x="728" y="4" width="22" height="110" fill="#141414"/>
    </svg>
    <div class="wordmark"><span class="mark"></span>VELOCITY</div>
    <p class="tagline">for <b>GAMERS</b><br>by <b>GAMERS</b></p>
  </section>

</div>
</body>
</html>
```